Varnel Supply requires a new business card.

We are an online professional tool store.

Target Market(s)

We target the professional technician.

Industry/Entity Type

Business

Contact Information for Business Card

VarnelSupply.com.au

sales@varnelsupply.example

Requirements
Must have
• Needs to look commercial and professional
Should not have
• No Australian Colors, maps or shapes.
• No Shapes of Tools

```html
<!DOCTYPE html>
<html lang="en">
<head>
<meta charset="utf-8">
<title>Varnel Supply – Business Card</title>
<link href="https://fonts.googleapis.com/css2?family=Orbitron:wght@500;700&family=Roboto:wght@400&display=swap" rel="stylesheet">
<style>
  :root{
    --stage:#2b2b2b;
    --paper:#f2f2f2;
    --brand-blue:#0c27ac;
    --brand-cyan:#1591c6;
    --ink:#444444;
    --white:#ffffff;
  }
  *{margin:0;padding:0;box-sizing:border-box;}
  html,body{width:1200px;height:960px;overflow:hidden;}
  body{background:var(--stage);position:relative;font-family:"Roboto",Arial,sans-serif;}

  .card{position:absolute;width:600px;height:343px;background:var(--paper);box-shadow:0 3px 8px rgba(0,0,0,.45);}
  .card--front{left:314px;top:113px;}
  .card--back{left:311px;top:472px;}

  .holder{position:absolute;left:41px;top:54px;font-family:"Orbitron",Arial,sans-serif;}
  .holder__name{font-size:21px;font-weight:500;color:var(--brand-blue);letter-spacing:.5px;line-height:1;}
  .holder__title{font-size:14px;font-weight:500;color:var(--brand-cyan);margin-top:7px;letter-spacing:.5px;line-height:1;}

  .wordmark{font-family:"Orbitron",Arial,sans-serif;font-weight:700;color:var(--brand-blue);line-height:1;white-space:nowrap;}
  .wordmark--front{position:absolute;right:36px;top:56px;font-size:28px;}
  .wordmark--back{position:absolute;left:0;right:0;top:148px;text-align:center;font-size:40px;}

  .contact-band{position:absolute;left:0;top:158px;width:600px;height:150px;
    background:linear-gradient(90deg,var(--brand-cyan) 0%,var(--brand-cyan) 4%,var(--brand-blue) 13%,var(--brand-blue) 100%);}
  .contact-list{position:absolute;right:36px;top:16px;list-style:none;text-align:right;color:var(--white);font-size:14.5px;line-height:18.5px;}
  .contact-list li{display:flex;justify-content:flex-end;align-items:center;gap:5px;}
  .contact-list li.gap{margin-top:5px;}
  .contact-list svg{width:13px;height:13px;fill:var(--white);flex:none;}

  .web{position:absolute;right:36px;bottom:10px;font-size:14px;color:var(--ink);letter-spacing:1.6px;}
  .web--back{left:0;right:0;bottom:37px;text-align:center;letter-spacing:3px;}
</style>
</head>
<body>

<section class="card card--front">
  <div class="holder">
    <p class="holder__name">DANA WHITFIELD</p>
    <p class="holder__title">CEO/FOUNDER</p>
  </div>
  <p class="wordmark wordmark--front">Varnel Supply</p>

  <div class="contact-band">
    <ul class="contact-list">
      <li>412 Marlow Street</li>
      <li>Brookvale, Ridgeway 20418</li>
      <li class="gap">555 210 4817
        <svg viewBox="0 0 16 16" aria-hidden="true"><path d="M3.5 1l2.5 3-1.5 2c1 2 3 4 5 5l2-1.5 3 2.5-1.5 2.5C8 15 1 8 1 2.5z"/></svg></li>
      <li>555 382 9046
        <svg viewBox="0 0 16 16" aria-hidden="true"><path d="M4 0h8v16H4zM5.5 2v10h5V2zM7 13.2h2v1.4H7z" fill-rule="evenodd"/></svg></li>
      <li>555 671 3025
        <svg viewBox="0 0 16 16" aria-hidden="true"><path d="M4 1h8v4H4zM1 6h14v6h-3v3H4v-3H1zM5.5 10v3.5h5V10z" fill-rule="evenodd"/></svg></li>
      <li>sales@varnelsupply.example
        <svg viewBox="0 0 16 16" aria-hidden="true"><path d="M1 3h14v10H1zM2.5 4.5v.6L8 9l5.5-3.9v-.6zM2.5 6.8v4.7h11V6.8L8 10.7z" fill-rule="evenodd"/></svg></li>
    </ul>
  </div>

  <p class="web">VarnelSupply.com.au</p>
</section>

<section class="card card--back">
  <p class="wordmark wordmark--back">Varnel Supply</p>
  <p class="web web--back">www.VarnelSupply.com.au</p>
</section>

</body>
</html>
```